New National Dermatology Group needs a business card!

We need a business card for our new national company that has 3 brands within the business:
Brindlewood Clinics Australia, Harrowmere Clinics Australia and Tallowfen Clinics Australia.
We help people access dermatology services close to home throughout Australia.
We need a business card that has:
all 3 logos on it,
Our websites (there are three, listed above)
Our email (there are three, listed above)
The location of our first clinic: 41 Wren St Parramatta (this can then be changed for each location as required)

```html
<!DOCTYPE html>
<html lang="en">
<head>
<meta charset="utf-8">
<title>Business Card – Harrowmere, Brindlewood &amp; Tallowfen Clinics Australia</title>
<link rel="stylesheet" href="https://fonts.googleapis.com/css2?family=Jost:wght@500&display=swap">
<style>
  :root {
    --stage: #b9b9b9;
    --card-dark-top: #2e2e2e;
    --card-dark-bottom: #0c0c0c;
    --card-light: #ffffff;
    --ink: #111111;
    --name-light: #f2f2f2;
    --band: #050505;
    --orange: #ee8a22;
    --green: #27a23a;
    --brown: #9a4f1a;
    --rule-dark: #3a3a3a;
  }
  * { box-sizing: border-box; margin: 0; padding: 0; }
  html, body { width: 1200px; height: 800px; overflow: hidden; }
  body {
    background: var(--stage);
    display: flex;
    align-items: center;
    justify-content: center;
    gap: 40px;
    font-family: "Jost", sans-serif;
  }
  .card {
    width: 520px;
    height: 300px;
    position: relative;
    overflow: hidden;
  }

  /* Front */
  .card--front {
    background: linear-gradient(160deg, var(--card-dark-top), var(--card-dark-bottom));
  }
  .card--front .edge-rule {
    position: absolute;
    left: 0; right: 0;
    height: 1px;
    background: var(--rule-dark);
  }
  .card--front .edge-rule--one { bottom: 34px; }
  .card--front .edge-rule--two { bottom: 28px; }
  .brand-list {
    position: absolute;
    left: 50%; top: 45%;
    transform: translate(-50%, -50%);
    list-style: none;
    display: flex;
    flex-direction: column;
    gap: 12px;
  }
  .brand {
    display: flex;
    align-items: center;
    gap: 10px;
    font-size: 18px;
    font-weight: 500;
    color: var(--name-light);
    line-height: 1;
    white-space: nowrap;
  }
  .brand__mark {
    width: 12px;
    height: 12px;
    flex: none;
  }
  .brand--harrowmere .brand__mark { background: var(--orange); }
  .brand--brindlewood .brand__mark { background: var(--green); }
  .brand--tallowfen .brand__mark { background: var(--brown); }

  /* Back */
  .card--back { background: var(--card-light); }
  .contact {
    position: absolute;
    left: 150px; top: 38px;
    width: 220px;
    display: flex;
    flex-direction: column;
    align-items: center;
  }
  .contact__label {
    font-size: 13px;
    font-weight: 500;
    color: var(--ink);
    margin-bottom: 6px;
  }
  .contact__line {
    width: 200px;
    height: 0;
    border-bottom: 2px dotted var(--ink);
    margin-bottom: 13px;
  }
  .contact__group { display: flex; flex-direction: column; align-items: center; margin-bottom: 6px; }
  .back-band {
    position: absolute;
    left: 0; right: 0; bottom: 0;
    height: 48px;
    background: var(--band);
  }
  .back-band__stripe {
    position: absolute;
    left: 0; right: 0; top: 10px;
    height: 3px;
    background: var(--card-light);
  }
</style>
</head>
<body>
  <section class="card card--front" aria-label="Card front">
    <ul class="brand-list">
      <li class="brand brand--harrowmere"><span class="brand__mark"></span>Harrowmere Clinics Australia</li>
      <li class="brand brand--brindlewood"><span class="brand__mark"></span>Brindlewood Clinics Australia</li>
      <li class="brand brand--tallowfen"><span class="brand__mark"></span>Tallowfen Clinics Australia</li>
    </ul>
    <span class="edge-rule edge-rule--one"></span>
    <span class="edge-rule edge-rule--two"></span>
  </section>

  <section class="card card--back" aria-label="Card back">
    <div class="contact">
      <div class="contact__group">
        <p class="contact__label">Web</p>
        <span class="contact__line"></span>
        <span class="contact__line"></span>
        <span class="contact__line"></span>
      </div>
      <div class="contact__group">
        <p class="contact__label">Email</p>
        <span class="contact__line"></span>
        <span class="contact__line"></span>
        <span class="contact__line"></span>
      </div>
      <div class="contact__group">
        <p class="contact__label">Location</p>
        <span class="contact__line"></span>
      </div>
    </div>
    <div class="back-band"><span class="back-band__stripe"></span></div>
  </section>
</body>
</html>
```